Gift Card/voucher Design for Beauty Clinic

I need a design for a gift card I Can use in all seasons for my Aesthetic clinic. The Logo is attached. The main colors we use are white and black, we are open for new suggestions to make an friendly yet professional impression. Ideally the gift card/voucher would be foldable.
The inside should contain the following fields:

Für:

Von:

Wert

Gültigkeit

```html
<!DOCTYPE html>
<html lang="de">
<head>
<meta charset="utf-8">
<title>Gift Card Design – Helena Brandt Aesthetics</title>
<link href="https://fonts.googleapis.com/css2?family=Oswald:wght@500;700&family=Kaushan+Script&family=Cormorant+Garamond:wght@600&display=swap" rel="stylesheet">
<style>
  :root {
    --board: #e0e0e0;
    --ink: #000000;
    --frame: #000000;
    --card: #ffffff;
    --pink: #f6c9cd;
    --pink-strong: #ee9aa3;
    --pink-text: #e0566a;
    --facet-light: #f7f6f6;
    --facet-mid: #e6e4e4;
  }
  * { margin: 0; padding: 0; box-sizing: border-box; }
  html, body { width: 1200px; height: 938px; overflow: hidden; }
  body {
    position: relative;
    background: var(--board);
    font-family: "Oswald", sans-serif;
    color: var(--ink);
  }
  .board-title {
    position: absolute; left: 0; top: 82px; width: 1200px;
    text-align: center; font-weight: 700; font-size: 84px; line-height: 1;
    letter-spacing: -1px;
  }
  .side-label {
    position: absolute; top: 218px; font-weight: 700; font-size: 34px; line-height: 1;
    letter-spacing: -0.5px;
  }
  .side-label--front { left: 26px; }
  .side-label--back { right: 26px; }

  .card {
    position: absolute; top: 270px; width: 569px; height: 407px;
    border: 8px solid var(--frame); background: var(--card); overflow: hidden;
  }
  .card--front { left: 26px; }
  .card--back { left: 606px; }

  /* front */
  .front-backdrop {
    position: absolute; inset: 0;
    background: linear-gradient(135deg, var(--facet-mid) 0%, var(--facet-light) 45%, var(--facet-mid) 70%, #ffffff 100%);
  }
  .brush-stroke {
    position: absolute; left: 0; top: 46px; width: 370px; height: 250px;
    background: radial-gradient(ellipse at 45% 45%, var(--pink-strong) 0%, var(--pink) 55%, rgba(246,201,205,0) 75%);
    opacity: 0.85;
  }
  .front-title {
    position: absolute; left: 0; width: 100%; top: 58px; text-align: center;
    font-family: "Kaushan Script", cursive; font-weight: 400; font-size: 88px; line-height: 1;
    padding-right: 30px;
  }
  .front-tagline {
    position: absolute; left: 0; width: 100%; top: 182px; text-align: center;
    font-family: "Kaushan Script", cursive; font-size: 30px; line-height: 1;
    padding-left: 20px; white-space: nowrap;
  }
  .wordmark {
    position: absolute; display: flex; align-items: center; gap: 8px;
    font-family: "Oswald", sans-serif; font-weight: 500; color: var(--ink);
    line-height: 1; white-space: nowrap;
  }
  .wordmark__dot {
    display: block; border-radius: 50%; background: var(--ink);
  }
  .card--front .wordmark {
    left: 0; width: 100%; justify-content: center; top: 278px; font-size: 22px;
  }
  .card--front .wordmark__dot { width: 12px; height: 12px; }

  /* back */
  .card--back .wordmark { left: 18px; top: 34px; font-size: 18px; }
  .card--back .wordmark__dot { width: 10px; height: 10px; }
  .details-title {
    position: absolute; left: 242px; top: 106px;
    font-family: "Kaushan Script", cursive; font-weight: 400; font-size: 32px; line-height: 1;
    white-space: nowrap;
  }
  .detail-row {
    position: absolute; left: 0; width: 100%; height: 34px;
  }
  .detail-row__label {
    position: absolute; left: 20px; top: 0; line-height: 34px;
    font-weight: 700; font-size: 27px; letter-spacing: -0.5px;
  }
  .detail-row__colon {
    position: absolute; left: 135px; top: 0; line-height: 34px;
    font-weight: 700; font-size: 22px;
  }
  .detail-row__field {
    position: absolute; left: 150px; top: 0; width: 344px; height: 34px;
    background: var(--pink);
  }
  .detail-row--for { top: 156px; }
  .detail-row--from { top: 199px; }
  .detail-row--value { top: 242px; }
  .detail-row--validity { top: 286px; }
  .expiry {
    position: absolute; left: 320px; top: 367px;
    font-family: "Cormorant Garamond", serif; font-weight: 600; font-size: 12px;
    color: var(--pink-text); display: flex; align-items: flex-end; gap: 6px;
    white-space: nowrap;
  }
  .expiry__blank { display: block; }

  .feature-list {
    position: absolute; left: 403px; top: 738px; list-style: none;
    font-weight: 500; font-size: 30px; line-height: 39px; letter-spacing: -0.3px;
  }
</style>
</head>
<body>
  <h1 class="board-title">Your Giftcard Design</h1>
  <p class="side-label side-label--front">Front Side</p>
  <p class="side-label side-label--back">Back Side</p>

  <section class="card card--front">
    <div class="front-backdrop" role="img" aria-label="Soft white and light grey faceted geometric background"></div>
    <div class="brush-stroke" role="img" aria-label="Pink watercolour brush stroke"></div>
    <h2 class="front-title">GiftCard</h2>
    <p class="front-tagline">For our remarkable example of beauty</p>
    <p class="wordmark"><span class="wordmark__dot"></span>Helena Brandt Aesthetics</p>
  </section>

  <section class="card card--back">
    <p class="wordmark"><span class="wordmark__dot"></span>Helena Brandt Aesthetics</p>
    <h2 class="details-title">GiftCard Details</h2>
    <div class="detail-row detail-row--for">
      <span class="detail-row__label">Für</span><span class="detail-row__colon">:</span><span class="detail-row__field"></span>
    </div>
    <div class="detail-row detail-row--from">
      <span class="detail-row__label">Von</span><span class="detail-row__colon">:</span><span class="detail-row__field"></span>
    </div>
    <div class="detail-row detail-row--value">
      <span class="detail-row__label">Wert</span><span class="detail-row__colon">:</span><span class="detail-row__field"></span>
    </div>
    <div class="detail-row detail-row--validity">
      <span class="detail-row__label">Gültigkeit</span><span class="detail-row__colon">:</span><span class="detail-row__field"></span>
    </div>
    <p class="expiry">
      <span>Giftcard Expiration Date:</span>
      <svg class="expiry__blank" width="96" height="14" viewBox="0 0 96 14" aria-hidden="true">
        <line x1="0" y1="13" x2="96" y2="13" stroke="#e0566a" stroke-width="1"/>
        <line x1="30" y1="12" x2="34" y2="1" stroke="#e0566a" stroke-width="1"/>
        <line x1="62" y1="12" x2="66" y2="1" stroke="#e0566a" stroke-width="1"/>
      </svg>
    </p>
  </section>

  <ul class="feature-list">
    <li>+ Print Ready (CYMK Color Profile)</li>
    <li>+ High Quality Prints</li>
    <li>+ Source File (Editable Format)</li>
  </ul>
</body>
</html>
```